Tolvane Air and Electrical Website

Simple and easy to use website for a Electrical and Air Conditioning contracting business.Use stock photosOnline contact portallogo still to be supplied

Target Market(s)

Mums and Dads who want a local contractor

Coding

Coded - Design and coding required

Number of Pages Required

2 page

Font styles to use
Sans Serif

Colors
f04a50
3276b5
33a6d7

Requirements
Must have
• Simple and easy to use
• Ph number
• 4 web address; linked to page
• 0417385926
• tolvane.com.au
• tolvaneelectrical.com.au
• tolvaneairandelectrical.com.au
• tolvaneair.com.au
Nice to have
• Split System Air Con Picture
• Electrical Pictures

```html
<!DOCTYPE html>
<html lang="en">
<head>
<meta charset="utf-8">
<title>Tolvane Air and Electrical</title>
<link rel="stylesheet" href="https://fonts.googleapis.com/css2?family=Roboto+Condensed:wght@400;700&family=Roboto:wght@400;500;700&display=swap">
<style>
:root{
  --red:#f04a50;
  --red-deep:#e0353d;
  --blue:#3276b5;
  --blue-nav:#2b64ad;
  --blue-dark:#1f4f8f;
  --sky:#33a6d7;
  --ink:#222;
  --body:#555;
  --light:#f4f5f8;
  --dark:#1a1a1c;
  --white:#fff;
}
*{box-sizing:border-box;margin:0;padding:0}
html,body{width:1200px;height:2881px;overflow:hidden}
body{position:relative;font-family:"Roboto",Arial,sans-serif;color:var(--body);background:var(--light)}
.abs{position:absolute}
.heading{font-family:"Roboto Condensed","Arial Narrow",sans-serif;font-weight:700;color:var(--ink);text-transform:uppercase}

/* header */
.site-header{left:0;top:0;width:1200px;height:97px;background:var(--white)}
.brand{left:145px;top:24px;font-family:"Roboto Condensed",sans-serif;font-weight:700;font-size:50px;line-height:50px;color:var(--red);letter-spacing:1px}
.call{right:145px;top:30px;display:flex;align-items:center;gap:10px;font-family:"Roboto Condensed",sans-serif;font-weight:700}
.call .label{color:var(--red);font-size:23px}
.call .num{color:var(--ink);font-size:30px}
.call-icon{width:38px;height:38px;border:2px solid var(--ink);border-radius:50%;display:flex;align-items:center;justify-content:center}

.main-nav{left:0;top:97px;width:1200px;height:47px;background:var(--blue-nav);display:flex;justify-content:center;gap:44px;align-items:center}
.main-nav a{color:var(--white);text-decoration:none;font-family:"Roboto Condensed",sans-serif;font-size:19px;text-transform:uppercase}

/* hero */
.hero{left:0;top:144px;width:1200px;height:631px;background:linear-gradient(100deg,#c9b9a6 0%,#ddd6cf 35%,#d8d3cf 55%,#8c8a8f 80%,#6f7f95 100%)}
.hero-title{left:0;top:252px;width:1200px;text-align:center;font-family:"Roboto Condensed",sans-serif;font-weight:700;font-size:94px;color:var(--white);letter-spacing:2px;text-shadow:0 2px 6px rgba(0,0,0,.25)}
.hero-sub{left:0;top:365px;width:1200px;text-align:center;font-size:20px;color:var(--white);text-shadow:0 1px 3px rgba(0,0,0,.4)}
.btn{display:inline-flex;align-items:center;justify-content:center;gap:8px;border-radius:30px;color:var(--white);font-family:"Roboto Condensed",sans-serif;font-weight:700;text-transform:uppercase;text-decoration:none}
.btn-red{background:var(--red)}
.btn-blue{background:var(--blue-nav);border:3px solid var(--white)}
.btn-line{border:3px solid var(--white)}
.arrow{width:13px;height:13px;border-radius:50%;background:currentColor;position:relative;display:inline-block}
.btn .arrow{background:var(--white)}
.arrow::after{content:"";position:absolute;left:3px;top:4px;border-left:6px solid var(--red);border-top:2.5px solid transparent;border-bottom:2.5px solid transparent}
.btn-blue .arrow::after{border-left-color:var(--blue-nav)}
.btn-line .arrow::after{border-left-color:var(--red)}
.dots{left:566px;top:632px;display:flex;gap:7px}
.dots span{width:8px;height:8px;border-radius:50%;background:var(--white)}
.dots span.on{background:var(--blue)}

/* about */
.about{left:0;top:775px;width:1200px;height:470px;background:var(--light)}
.ghost{font-family:"Roboto Condensed",sans-serif;font-weight:700;color:rgba(0,0,0,.07);text-transform:uppercase}
.about-ghost{left:-95px;top:965px;font-size:86px;transform:rotate(-90deg);transform-origin:center;width:360px;text-align:center}
.about-title{left:145px;top:800px;font-size:42px}
.copy{font-size:12.5px;line-height:29.6px;color:var(--body)}
.about-copy{left:145px;top:858px;width:480px}
.about-photo-ring{left:658px;top:788px;width:392px;height:392px;border-radius:50%;background:var(--blue-dark)}
.about-photo{left:652px;top:785px;width:386px;height:386px;border-radius:50%;border:4px solid var(--white);background:radial-gradient(circle at 45% 40%,#c9a58e 0%,#3a5fc2 45%,#2a4aa8 70%,#6d6a6a 100%)}

/* services */
.services{left:0;top:1191px;width:1200px;height:518px}
.svc-title{color:var(--white);font-size:40px}
.svc-copy{color:var(--white);width:400px}

/* blog */
.blog-ghost{left:0;top:1740px;width:1200px;text-align:center;font-size:100px;color:rgba(0,0,0,.08)}
.blog-title{left:0;top:1795px;width:1200px;text-align:center;font-size:43px}
.post{width:279px}
.post-img{width:279px;height:166px;position:relative}
.date{position:absolute;right:0;bottom:0;width:61px;height:57px;background:var(--blue-nav);color:var(--white);font-family:"Roboto Condensed",sans-serif;font-weight:700;font-size:20px;line-height:20px;text-align:center;padding-top:8px}
.post-title{margin-top:28px;font-size:21px}
.post-copy{margin-top:12px;font-size:11.5px;line-height:20.5px}
.post .btn{margin-top:19px;width:133px;height:39px;font-size:12px}

/* contact */
.contact-ghost{left:940px;top:2505px;font-size:80px;color:rgba(255,255,255,.06);transform:rotate(-90deg);width:420px;text-align:center}
.contact-title{left:0;top:2455px;width:1200px;text-align:center;font-size:43px;color:var(--white)}
.sub-head{font-size:16px;font-weight:500;color:var(--white)}
.field{background:var(--white);border:1px solid #ccc;font-size:11px;color:#666;padding:8px 11px;text-transform:uppercase}
.submit{left:609px;top:2742px;width:78px;height:28px;border-radius:14px;background:var(--blue-nav);color:var(--white);font-size:12px;font-weight:700;display:flex;align-items:center;justify-content:center}
.info-row{display:flex;align-items:center;gap:17px;color:var(--white);font-size:12px;line-height:17px}
.info-icon{width:34px;height:34px;border:2px solid var(--white);border-radius:50%;display:flex;align-items:center;justify-content:center;flex:none}
.socials{left:759px;top:2720px;display:flex;gap:7px}
.socials span{width:27px;height:27px;border-radius:50%}
.rule{left:132px;top:2820px;width:936px;height:1px;background:rgba(255,255,255,.15)}
.copyright{left:0;top:2848px;width:1200px;text-align:center;color:var(--white);font-size:12px}
</style>
</head>
<body>

<header class="abs site-header">
  <div class="abs brand">TOLVANE</div>
  <div class="abs call">
    <span class="call-icon"><svg width="20" height="20" viewBox="0 0 24 24"><path d="M6.6 10.8a15.1 15.1 0 0 0 6.6 6.6l2.2-2.2a1 1 0 0 1 1-.25 11.4 11.4 0 0 0 3.6.57 1 1 0 0 1 1 1V20a1 1 0 0 1-1 1A17 17 0 0 1 3 4a1 1 0 0 1 1-1h3.5a1 1 0 0 1 1 1c0 1.25.2 2.45.57 3.57a1 1 0 0 1-.25 1z" fill="#222"/></svg></span>
    <span class="label">CALL US :</span><span class="num">0417385926</span>
  </div>
</header>

<nav class="abs main-nav">
  <a href="#">Home</a><a href="#">About Us</a><a href="#">Services</a><a href="#">News</a><a href="#">Contact Us</a>
</nav>

<section class="abs hero" role="img" aria-label="Stock photo of a woman relaxing on a sofa under a split system air conditioner"></section>
<h1 class="abs hero-title">TOLVANE</h1>
<p class="abs hero-sub">Sed ut perspiciatis unde omnis iste natus error siatem accusantium</p>
<a class="abs btn btn-red" href="#" style="left:430px;top:425px;width:165px;height:48px;font-size:15px">Read More <i class="arrow"></i></a>
<a class="abs btn btn-blue" href="#" style="left:605px;top:425px;width:165px;height:48px;font-size:15px">Get Started <i class="arrow"></i></a>
<div class="abs dots"><span></span><span></span><span class="on"></span><span></span><span></span></div>

<section class="abs about"></section>
<svg class="abs" style="left:0;top:650px" width="1200" height="130" viewBox="0 0 1200 130">
  <polygon points="0,125 288,10 1200,125 1200,130 0,130" fill="var(--light)"/>
  <polyline points="0,125 288,10 1200,125" fill="none" stroke="var(--red)" stroke-width="7"/>
</svg>
<div class="abs ghost about-ghost">About</div>
<h2 class="abs heading about-title">About Us</h2>
<p class="abs copy about-copy">At vero eos et accusamus et iusto odio dignissimos ducimus qui blanditiis praesentium voluptatum deleniti atque corrupti quos dolores et quas molestias excepturi sint occaecati cupiditate non provident, similique sunt in culpa qui officia deserunt mollitia animi, id est laborum et dolorum fuga. Et harum quidem rerum facilis est et expedita distinctio. Nam libero tempore, cum soluta nobis est eligendi optio cumque nihil impedit quo minus id quod maxime placeat facere possimus</p>
<a class="abs btn btn-red" href="#" style="left:145px;top:1059px;width:165px;height:49px;font-size:15px">Read More <i class="arrow"></i></a>
<div class="abs about-photo-ring"></div>
<div class="abs about-photo" role="img" aria-label="Stock photo of an electrician in a blue hard hat working at a switchboard"></div>

<section class="abs services">
  <svg width="1200" height="518" viewBox="0 0 1200 518">
    <polygon points="0,95 145,0 600,95 600,518 0,518" fill="#3d72b0"/>
    <polygon points="600,95 1055,0 1200,95 1200,518 600,518" fill="#ec545a"/>
  </svg>
</section>
<h2 class="abs heading svc-title" style="left:74px;top:1361px">Electrical</h2>
<p class="abs copy svc-copy" style="left:74px;top:1421px">At vero eos et accusamus et iusto odio dignissimos ducimus qui blanditiis praesentium voluptatum deleniti atque corrupti quos dolores et quas molestias excepturi sint occaecati cupiditate non provident, similique sunt in culpa qui officia deserunt mollitia</p>
<a class="abs btn btn-red" href="#" style="left:74px;top:1568px;width:164px;height:48px;font-size:15px;border:2px solid var(--white)">Read More <i class="arrow"></i></a>
<h2 class="abs heading svc-title" style="left:673px;top:1356px">Air Conditioning</h2>
<p class="abs copy svc-copy" style="left:673px;top:1416px">At vero eos et accusamus et iusto odio dignissimos ducimus qui blanditiis praesentium voluptatum deleniti atque corrupti quos dolores et quas molestias excepturi sint occaecati cupiditate non provident, similique sunt in culpa qui officia deserunt mollitia</p>
<a class="abs btn btn-line" href="#" style="left:673px;top:1573px;width:164px;height:48px;font-size:15px">Read More <i class="arrow"></i></a>

<div class="abs ghost blog-ghost">Blog</div>
<h2 class="abs heading blog-title">Blog Posts</h2>

<article class="abs post" style="left:144px;top:1902px">
  <div class="post-img" role="img" aria-label="Stock photo of a yellow insulation tester with test leads" style="background:linear-gradient(135deg,#3a3a3a,#d9b21a 55%,#555)"><div class="date">JUN<br>03</div></div>
  <h3 class="heading post-title">Blog Title Here</h3>
  <p class="post-copy">At vero eos et accusamus et iusto odio dignissimos ducimus qui blanditiis praesentium voluptatum deleniti atque corrupti quo</p>
  <a class="btn btn-red" href="#">Read More <i class="arrow"></i></a>
</article>
<article class="abs post" style="left:461px;top:1902px">
  <div class="post-img" role="img" aria-label="Stock photo of a contractor shaking hands with a couple" style="background:linear-gradient(135deg,#6c86a8,#e6e6ea 50%,#43516a)"><div class="date">JUN<br>03</div></div>
  <h3 class="heading post-title">Blog Title Here</h3>
  <p class="post-copy">At vero eos et accusamus et iusto odio dignissimos ducimus qui blanditiis praesentium voluptatum deleniti atque corrupti quo</p>
  <a class="btn btn-red" href="#">Read More <i class="arrow"></i></a>
</article>
<article class="abs post" style="left:776px;top:1902px">
  <div class="post-img" role="img" aria-label="Stock photo of a hand holding a multimeter at a power outlet" style="background:linear-gradient(135deg,#8a8a8a,#d8a23c 45%,#3c4f86)"><div class="date">JUN<br>03</div></div>
  <h3 class="heading post-title">Blog Title Here</h3>
  <p class="post-copy">At vero eos et accusamus et iusto odio dignissimos ducimus qui blanditiis praesentium voluptatum deleniti atque corrupti quo</p>
  <a class="btn btn-red" href="#">Read More <i class="arrow"></i></a>
</article>

<svg class="abs" style="left:0;top:2296px" width="1200" height="585" viewBox="0 0 1200 585">
  <polygon points="0,4 911,123 1200,4 1200,585 0,585" fill="var(--dark)"/>
  <polyline points="0,4 911,123 1200,4" fill="none" stroke="var(--red)" stroke-width="6"/>
</svg>
<div class="abs ghost contact-ghost">Contact</div>
<h2 class="abs heading contact-title">Contact Us</h2>

<div class="abs sub-head" style="left:143px;top:2534px">Get In Touch:</div>
<div class="abs field" style="left:145px;top:2575px;width:265px;height:29px">Name :</div>
<div class="abs field" style="left:422px;top:2575px;width:265px;height:29px">Phone :</div>
<div class="abs field" style="left:145px;top:2616px;width:542px;height:29px">Email :</div>
<div class="abs field" style="left:145px;top:2656px;width:542px;height:66px">Message :</div>
<div class="abs submit">SUBMIT</div>

<div class="abs sub-head" style="left:757px;top:2534px">Contact Information</div>
<div class="abs info-row" style="left:757px;top:2575px">
  <span class="info-icon"><svg width="14" height="16" viewBox="0 0 24 24"><path d="M12 2a7 7 0 0 0-7 7c0 5 7 13 7 13s7-8 7-13a7 7 0 0 0-7-7zm0 9.5A2.5 2.5 0 1 1 12 6.5a2.5 2.5 0 0 1 0 5z" fill="#fff"/></svg></span>
  <span>23.am libero temporeum solut<br>nobis est elig</span>
</div>
<div class="abs info-row" style="left:757px;top:2626px">
  <span class="info-icon"><svg width="14" height="14" viewBox="0 0 24 24"><path d="M6.6 10.8a15.1 15.1 0 0 0 6.6 6.6l2.2-2.2a1 1 0 0 1 1-.25 11.4 11.4 0 0 0 3.6.57 1 1 0 0 1 1 1V20a1 1 0 0 1-1 1A17 17 0 0 1 3 4a1 1 0 0 1 1-1h3.5a1 1 0 0 1 1 1c0 1.25.2 2.45.57 3.57a1 1 0 0 1-.25 1z" fill="#fff"/></svg></span>
  <span>Contact - 0417385926</span>
</div>
<div class="abs info-row" style="left:757px;top:2669px">
  <span class="info-icon"><svg width="15" height="12" viewBox="0 0 24 18"><rect x="0" y="0" width="24" height="18" rx="2" fill="#fff"/><path d="M1 2l11 8 11-8" fill="none" stroke="#1a1a1c" stroke-width="2"/></svg></span>
  <span>info@companyname.com</span>
</div>
<div class="abs socials">
  <span style="background:#2b4f9e"></span><span style="background:#1da1f2"></span><span style="background:#e52d27"></span><span style="background:#a27b4a"></span><span style="background:#0e76a8"></span>
</div>

<div class="abs rule"></div>
<div class="abs copyright">Copyrights © 2019, Companyname. All Rights Reserved. &nbsp;|&nbsp; Privacy policy</div>

</body>
</html>
```